Website for Sports and Exercise Medicine Doctor with active research in stem cells therapies.

I am a sports and exercise medicine doctor with research interests in the cutting edge areas of biological therapies, most notable stem cells. None of my patients are dying of anything, and most of them come to see me to decrease their pain, so they can get back to what they want to do.

The approach i then take is to decrease their pain and support them to achieve the things they wish to achieve. Most people start at "Just make it stop hurting doc" , but I try to move them towards something more important over time.

I would like the website to be very different to other "Doctor or medical websites" in its look. No pictures of doctors in white coats and no pictures of fit old people smiling. I would potentially like the fist thing seen to be a quote:

"Less pain. Everybody wants it, but what are you going to do, once you've got it?"

(But this is only an idea, I am open to anything)

The website will need a couple of things

1. "Locations" I work
2. "Research" I am involved in
3. "Sort Me out" - Clinical information for people to access
4. "Social" - imbedded twitter and facebook
5. "Blog" - imbedded wordpress blog
6. "Bio" - the usual bio-stuff

The "Sort Me out" - pages I would like to have the functionality as seen in this site http://www.veltarion.com.au/platelet/. I intend to put disease topics into these pages (eg Achilles tehdinopathy, osteoarthritis etc etc etc). Once again I am not wedded to this but something along these lines would be good.

To give you an idea these are some sites I like
http://www.morbanquilt.com/
http://daptrine.com/
http://ovimbera.com.sg/
http://jolvaniketchup.com/
http://www.pilnorwave.com/
http://quadrisel.com/#offering
http://fennikstudio.tv/
http://norvalgate.com/
http://sablethorn.co.uk/#about

Target Market(s)

20-80 year old.
People with tendon injuries
People with osteoarthritis
People interested in stem cells
I will build the site over time to contain information on multiple sporting injuries and musculoskeletal disorders. It will also become a site for the latest on stem cell research particularly in the area of osteoarthritis.

Industry/Entity Type

Medical

Font styles to use
Sans Serif

Colors
ffffff

Requirements
Nice to have
• To give you an idea these are some sites I like
http://daptrine.com/
http://fennikstudio.tv/
http://norvalgate.com/
Should not have
• Pictures of doctors in white coats or old fit people smiling

```html
<!DOCTYPE html>
<html lang="en">
<head>
<meta charset="utf-8">
<title>Orvella — Sports and Exercise Medicine</title>
<link href="https://fonts.googleapis.com/css2?family=Questrial&family=Ubuntu:wght@700&display=swap" rel="stylesheet">
<style>
  :root {
    --header-blue: #8db6d5;
    --header-line: #a9c9e2;
    --hero-deep: #1f5a85;
    --hero-mid: #4f88b6;
    --hero-soft: #7fa9c4;
    --circle-fill: #8fb8d7;
    --circle-rim: #b4d1e6;
    --button-teal: #2f7c93;
    --button-edge: #1d5d70;
    --footer-navy: #0c3553;
    --white: #ffffff;
  }
  * { box-sizing: border-box; margin: 0; padding: 0; }
  html, body { width: 1200px; height: 749px; overflow: hidden; }
  body { font-family: "Questrial", sans-serif; color: var(--white); background: var(--footer-navy); }
  .page { position: relative; width: 1200px; height: 749px; }

  .site-header {
    position: absolute; top: 0; left: 0; width: 1200px; height: 108px;
    background: var(--header-blue);
  }
  .brand {
    position: absolute; left: 98px; top: 30px;
    display: flex; align-items: center; gap: 10px;
    font-size: 40px; letter-spacing: 1px; color: var(--white);
  }
  .brand-dot { width: 12px; height: 12px; border-radius: 50%; background: var(--white); }

  .main-nav { position: absolute; left: 578px; top: 0; height: 108px; display: flex; }
  .nav-item {
    width: 89.5px; height: 108px; border-left: 1px solid var(--header-line);
    display: flex; flex-direction: column; align-items: center; justify-content: flex-start;
    color: var(--white); text-decoration: none; font-size: 11.5px; letter-spacing: .3px;
  }
  .nav-item:last-child { border-right: none; }
  .nav-icon { width: 30px; height: 30px; margin-top: 34px; margin-bottom: 7px; }

  .hero {
    position: absolute; top: 108px; left: 0; width: 1200px; height: 590px;
    background:
      radial-gradient(circle at 15% 55%, var(--hero-mid) 0, #3e78a8 22%, transparent 42%),
      radial-gradient(circle at 70% 25%, #5e8fb2 0, transparent 18%),
      radial-gradient(circle at 84% 62%, #5a8db6 0, transparent 12%),
      linear-gradient(110deg, #5d95bf 0%, var(--hero-soft) 55%, #50809f 100%);
  }
  .quote-disc {
    position: absolute; left: 439px; top: 64px; width: 332px; height: 332px;
    border-radius: 50%; background: var(--circle-fill);
    border: 3px solid var(--circle-rim);
    box-shadow: 0 3px 10px rgba(20, 60, 90, .35);
    text-align: center;
  }
  .quote-text {
    margin-top: 88px; font-size: 26px; line-height: 30px; font-weight: 400;
  }
  .quote-button {
    display: inline-block; margin-top: 24px;
    width: 166px; height: 35px; line-height: 35px;
    background: var(--button-teal); border: 1px solid var(--button-edge);
    border-radius: 2px; box-shadow: 0 2px 3px rgba(0,0,0,.3);
    font-family: "Ubuntu", sans-serif; font-weight: 700; font-size: 17px; letter-spacing: .5px;
    color: var(--white); text-decoration: none;
  }

  .site-footer {
    position: absolute; top: 698px; left: 0; width: 1200px; height: 51px;
    background: var(--footer-navy); font-size: 10.5px; letter-spacing: .2px;
  }
  .copyright { position: absolute; left: 91px; top: 23px; }
  .footer-nav { position: absolute; right: 89px; top: 19px; }
  .footer-nav a { color: var(--white); text-decoration: none; }
</style>
</head>
<body>
<div class="page">
  <header class="site-header">
    <div class="brand"><span class="brand-dot"></span>orvella</div>
    <nav class="main-nav">
      <a class="nav-item" href="#sort-me-out">
        <svg class="nav-icon" viewBox="0 0 30 30" fill="none" stroke="#fff" stroke-width="2.2">
          <path d="M5 8v16h20V8" /><path d="M15 4v13" /><path d="M11 8l4-4 4 4" />
          <rect x="9" y="14" width="12" height="10" fill="#fff" stroke="none"/>
        </svg>SORT ME OUT</a>
      <a class="nav-item" href="#bio">
        <svg class="nav-icon" viewBox="0 0 30 30" fill="#fff">
          <path d="M12 3h6v2h-1v7l7 12a2 2 0 0 1-2 3H8a2 2 0 0 1-2-3l7-12V5h-1z"/>
        </svg>BIO</a>
      <a class="nav-item" href="#locations">
        <svg class="nav-icon" viewBox="0 0 30 30" fill="none" stroke="#fff" stroke-width="1.8">
          <path d="M3 7l7-3 10 3 7-3v19l-7 3-10-3-7 3z"/><path d="M10 4v19M20 7v7"/>
          <circle cx="21" cy="18" r="3" fill="#fff"/><path d="M21 21v5"/>
        </svg>LOCATIONS</a>
      <a class="nav-item" href="#research">
        <svg class="nav-icon" viewBox="0 0 30 30" fill="#fff">
          <circle cx="15" cy="11" r="7" fill="none" stroke="#fff" stroke-width="2"/>
          <circle cx="15" cy="10" r="2.5"/><circle cx="5" cy="15" r="2.5"/><circle cx="25" cy="15" r="2.5"/>
          <rect x="3" y="19" width="4" height="6"/><rect x="23" y="19" width="4" height="6"/><rect x="13" y="20" width="4" height="6"/>
        </svg>RESEARCH</a>
      <a class="nav-item" href="#social">
        <svg class="nav-icon" viewBox="0 0 30 30" fill="none" stroke="#fff" stroke-width="1.8">
          <circle cx="15" cy="15" r="11"/><ellipse cx="15" cy="15" rx="5" ry="11"/><path d="M4 15h22M6 9h18M6 21h18"/>
        </svg>SOCIAL</a>
      <a class="nav-item" href="#blog">
        <svg class="nav-icon" viewBox="0 0 30 30" fill="#fff">
          <circle cx="15" cy="18" r="9"/>
        </svg>BLOG</a>
    </nav>
  </header>

  <main class="hero" role="img" aria-label="Close-up of translucent blue stem cells with water droplets">
    <section class="quote-disc">
      <p class="quote-text">Less pain. Everybody<br>wants it, but what<br>are you going to do,<br>once you’ve got it?</p>
      <a class="quote-button" href="#quote">GET QUOTE NOW</a>
    </section>
  </main>

  <footer class="site-footer">
    <p class="copyright">COPYRIGHT 2013 ORVELLA.COM</p>
    <nav class="footer-nav">
      <a href="#sort-me-out">SORT ME OUT</a> | <a href="#locations">LOCATIONS</a> | <a href="#research">RESEARCH</a> | <a href="#social">SOCIAL</a> | <a href="#blog">BLOG</a> | <a href="#bio">BIO</a>
    </nav>
  </footer>
</div>
</body>
</html>
```